Verantix - Solution provider in business consulting

Verantix is a swiss based company providing solutions for developing markets. The business covers various fields of business consulting, such as supply chain, product costs, quality management and manufacturing management. The Business operates in a efficient, straight and solution oriented manner.
The final design should communicate these characteristics. Asian people as well as as western people shall identify the qualities of the company at first sight.
The customer needs business cards with a simple view but an recognizable design, printed in high quality. Engraved elements such as the globe or simple words are possible.
Available colors are: (RAL)
102/102/102
51/102/102
153/204/153
255/102/51
Font: Calibri
Industry/Entity Type
Business
Look and feel
Each slider illustrates characteristics of the customer's brand and the style your logo design should communicate.

```html
<!DOCTYPE html>
<html lang="en">
<head>
<meta charset="utf-8">
<title>Verantix – Business Card</title>
<link rel="stylesheet" href="https://fonts.googleapis.com/css2?family=Open+Sans:wght@300;400;600&display=swap">
<style>
  :root {
    --stage: #dcd9d5;
    --card: #666666;
    --ink: #f4f4f4;
    --ink-soft: #e6e6e6;
    --rule: #d0d0d0;
  }
  * { margin: 0; padding: 0; box-sizing: border-box; }
  html, body {
    width: 1200px;
    height: 1000px;
    overflow: hidden;
    background: var(--stage);
    font-family: "Open Sans", Calibri, sans-serif;
  }
  .business-card {
    position: absolute;
    left: 101px;
    top: 201px;
    width: 998px;
    height: 597px;
    background: var(--card);
    border-radius: 33px;
    color: var(--ink);
  }
  .holder {
    position: absolute;
    left: 48px;
    top: 150px;
  }
  .holder-name {
    font-weight: 600;
    font-size: 33px;
    line-height: 1.1;
  }
  .holder-role {
    font-weight: 400;
    font-size: 25px;
    line-height: 1.3;
    color: var(--ink-soft);
  }
  .brand-name {
    position: absolute;
    right: 50px;
    top: 88px;
    font-weight: 300;
    font-size: 76px;
    line-height: 1;
    letter-spacing: 1px;
    color: var(--ink);
  }
  .company-address {
    position: absolute;
    right: 50px;
    top: 280px;
    text-align: right;
    font-size: 25px;
    line-height: 33px;
    font-style: normal;
  }
  .contact-list {
    position: absolute;
    right: 50px;
    top: 397px;
    list-style: none;
    text-align: right;
    font-size: 25px;
    line-height: 37px;
  }
  .contact-item {
    display: flex;
    justify-content: flex-end;
    align-items: center;
    gap: 10px;
  }
  .contact-icon {
    width: 20px;
    height: 20px;
    fill: var(--ink);
  }
  .card-footer {
    position: absolute;
    left: 48px;
    right: 50px;
    top: 520px;
    display: flex;
    align-items: center;
    gap: 16px;
    font-size: 25px;
  }
  .web-address { white-space: nowrap; }
  .web-address strong { font-weight: 600; }
  .footer-rule {
    flex: 1;
    height: 2px;
    background: var(--rule);
    margin-top: 4px;
  }
</style>
</head>
<body>
  <article class="business-card">
    <div class="holder">
      <p class="holder-name">Marco Lindt</p>
      <p class="holder-role">CEO</p>
    </div>

    <p class="brand-name">verantix</p>

    <address class="company-address">
      Verantix GmbH<br>
      Feldweg 14<br>
      8450 Talbach
    </address>

    <ul class="contact-list">
      <li class="contact-item">+41 79 382 5610
        <svg class="contact-icon" viewBox="0 0 20 20" aria-hidden="true"><rect x="6" y="1" width="8" height="18" rx="1.5"/><rect x="7.5" y="3.5" width="5" height="6" fill="#666"/></svg>
      </li>
      <li class="contact-item">+41 71 604 2917
        <svg class="contact-icon" viewBox="0 0 20 20" aria-hidden="true"><path d="M2 7c0-2 3.5-3.5 8-3.5S18 5 18 7v1.5h-4V6.8H6v1.7H2z"/><path d="M5 10h10l2 7H3z"/></svg>
      </li>
      <li class="contact-item">marco.lindt@verantix.ch
        <svg class="contact-icon" viewBox="0 0 20 20" aria-hidden="true"><rect x="1" y="4" width="18" height="12"/><path d="M1.5 4.5 10 11l8.5-6.5" fill="none" stroke="#666" stroke-width="1.5"/></svg>
      </li>
    </ul>

    <footer class="card-footer">
      <span class="web-address">www.<strong>verantix</strong>.ch</span>
      <span class="footer-rule"></span>
    </footer>
  </article>
</body>
</html>
```